Healthy Snack/Confectionery Bar Logo & front of pack

KOVA LUMEN LOGO and ON PACK
Directionally, use of colours specified in the brief is important as consumers associate the brand values we want with these colours. Blue. Green Cyan on White background should probably be the base colours. Gradients and Swirls of Colour would be good, but welcome alternatives. Product imagery should be in a set window that works well with the logo design.

Core Target Audience: Adults seeking to reduce/avoid sugar due to health concerns (pre-diabetic/diabetic/sugar avoiders), Secondary Audiences: Healthcare professionals looking for strategies to reduce sugar consumption, Mothers seeking to reduce family sugar consumption. Core Design Objectives: “HEALTHY AND PREMIUM” “FRESH” / Tasty / Appetising (product illustration) / Premium, Natural and Low in Sugar (colour cues) / Expert / Effective / Recommended (endorsements and back of pack).
Cyan/Blue often used to denote No added Sugar. Cyan = R 0 G 255 B 255
Blue/Green often used to denote medical benefit. Blue= R 0 G 129 B 129 / Green= R 132 G 173 B 0
Kova Lumen Yellow – R 254 G 244 B 0 links to QRB Brand.
* RGB Values for Cyan and Blue and Green are for Guidance only.

Text & Fonts: No more than 6 words. Largest - KOVA LUMEN (SUGAR to be subservient / more in the background - LUMEN should stand out as the main word. Medium - PELLOW DRIFT - Medium & integrated into design - LOW SUGAR
Fonts Decorative – e.g. MICROBREW, PHOPSPHATE, CAMPUS, INTRO RUST, BURFORD RUSTIC (see glyphhaven.net)

Target Market(s)

UK / NORTHERN EUROPE / AFLLUENT

Font styles to use
Sans Serif
Decorative

Colors
ffffff
0455a3
add136
fbee3d
000000
34a7d8

Requirements
Must have
• The design is for a healthy snack bar logo. Ideally the files submitted should include the image in an on-pack situation (e.g. a cereal bar, flapjack or cookie)
Nice to have
• See brief.

```html
<!DOCTYPE html>
<html lang="en">
<head>
<meta charset="utf-8">
<title>Kova Lumen – Pellow Drift front of pack</title>
<link href="https://fonts.googleapis.com/css2?family=Fredoka:wght@600;700&family=Josefin+Sans:wght@600&display=swap" rel="stylesheet">
<style>
  :root {
    --page: #ffffff;
    --wrapper-teal: #79c6cc;
    --wrapper-teal-mid: #6dbfc5;
    --wrapper-teal-deep: #5fb3ba;
    --pattern-teal: #4fa9b1;
    --label-white: #ffffff;
    --brand-teal: #6ccbd0;
    --leaf-green: #b8dd96;
    --badge-green: #a8d37a;
  }
  html, body {
    margin: 0;
    width: 1200px;
    height: 1000px;
    overflow: hidden;
    background: var(--page);
  }
  .canvas {
    display: block;
    width: 1200px;
    height: 1000px;
  }
  .brand-name {
    font-family: "Fredoka", sans-serif;
    font-weight: 700;
    fill: var(--brand-teal);
  }
  .brand-name__first { font-size: 74px; }
  .brand-name__second { font-size: 106px; letter-spacing: 1px; }
  .flavour-name {
    font-family: "Josefin Sans", sans-serif;
    font-weight: 600;
    font-size: 26px;
    letter-spacing: 2.5px;
    fill: var(--label-white);
  }
  .claim-text {
    font-family: "Fredoka", sans-serif;
    font-weight: 600;
    font-size: 25px;
    fill: var(--badge-green);
  }
</style>
</head>
<body>
<svg class="canvas" viewBox="0 0 1200 1000" xmlns="http://www.w3.org/2000/svg">
  <defs>
    <linearGradient id="wrapper-fill" x1="0" y1="0" x2="0" y2="1">
      <stop offset="0" stop-color="#79c6cc"/>
      <stop offset="0.55" stop-color="#6fc0c6"/>
      <stop offset="1" stop-color="#60b4bb"/>
    </linearGradient>
    <linearGradient id="pattern-wash" x1="0" y1="0" x2="1" y2="1">
      <stop offset="0" stop-color="#4fa9b1" stop-opacity="0.18"/>
      <stop offset="0.5" stop-color="#4fa9b1" stop-opacity="0.08"/>
      <stop offset="1" stop-color="#4fa9b1" stop-opacity="0.2"/>
    </linearGradient>
    <pattern id="crimp-left" patternUnits="userSpaceOnUse" x="122" y="300" width="14" height="18">
      <polygon points="14,0 0,9 14,18" fill="#6fc0c6"/>
    </pattern>
    <pattern id="crimp-right" patternUnits="userSpaceOnUse" x="1054" y="300" width="14" height="18">
      <polygon points="0,0 14,9 0,18" fill="#6fc0c6"/>
    </pattern>
  </defs>

  <g class="pack-front">
    <rect class="pack-front__crimp" x="122" y="300" width="14" height="360" fill="url(#crimp-left)"/>
    <rect class="pack-front__crimp" x="1054" y="300" width="14" height="360" fill="url(#crimp-right)"/>
    <path class="pack-front__body" d="M135,300 Q300,306 600,306 Q900,306 1055,300 L1055,660 Q900,648 600,648 Q300,648 135,660 Z" fill="url(#wrapper-fill)"/>
    <path class="pack-front__pattern" role="img" aria-label="Scattered teal brush-stroke sprinkle pattern across the wrapper"
          d="M135,300 Q300,306 600,306 Q900,306 1055,300 L1055,660 Q900,648 600,648 Q300,648 135,660 Z" fill="url(#pattern-wash)"/>

    <g class="brand-label">
      <rect x="276" y="362" width="389" height="280" fill="var(--label-white)"/>
      <text class="brand-name" aria-label="Kova Lumen">
        <tspan class="brand-name__first" x="294" y="458">Kova</tspan>
        <tspan class="brand-name__second" x="470" y="546" text-anchor="middle">LUMEN</tspan>
      </text>
      <path class="flavour-banner" d="M305,566 Q470,560 637,562 L629,581 L637,602 Q470,596 305,600 L311,583 Z" fill="var(--leaf-green)"/>
      <text class="flavour-name" x="471" y="592" text-anchor="middle">PELLOW DRIFT</text>
    </g>

    <g class="claim-badge" transform="rotate(-6 888 415)">
      <ellipse cx="888" cy="415" rx="43" ry="53" fill="var(--label-white)"/>
      <text class="claim-text" x="888" y="410" text-anchor="middle">LOW</text>
      <text class="claim-text" x="888" y="440" text-anchor="middle">SUGAR</text>
    </g>
    <rect class="claim-badge__basket" role="img" aria-label="Small line drawing of a balloon basket hanging below the low sugar badge"
          x="884" y="472" width="38" height="70" rx="10" fill="#ffffff" fill-opacity="0.22"/>
  </g>
</svg>
</body>
</html>
```